Business Card Design Project

We are an agricultural business based in Brisbane.
We design, manage and operate regional saleyards. Our logo is green/silver in colour and details of our business can be found on our website www.vodemarketyards.com.au

Just wanting a corporate design for some business cards and include name, position, contact details.

Thanks

Industry/Entity Type

Business

```html
<!DOCTYPE html>
<html lang="en">
<head>
<meta charset="utf-8">
<title>Vode Market Yards – Business Cards</title>
<link rel="stylesheet" href="https://fonts.googleapis.com/css2?family=Exo+2:wght@500;600;800&display=swap">
<style>
  :root {
    --stage-light: #8cc400;
    --stage-mid: #6fa800;
    --stage-dark: #3f7200;
    --brand-green: #00703c;
    --text-dark: #1a1a1a;
    --text-grey: #7a7a7a;
    --card-white: #ffffff;
    --pattern-tint: #eef6f0;
    --pattern-line: #cfe6d6;
  }
  * { margin: 0; padding: 0; box-sizing: border-box; }
  html, body { width: 1200px; height: 772px; overflow: hidden; }
  body {
    position: relative;
    font-family: "Exo 2", sans-serif;
    background: radial-gradient(ellipse at 45% 40%, var(--stage-light) 0%, var(--stage-mid) 50%, var(--stage-dark) 100%);
  }
  .card {
    position: absolute;
    width: 331px;
    height: 203px;
    background: var(--card-white);
    overflow: hidden;
  }
  .card--back { left: 244px; top: 279px; }
  .card--front-md { left: 626px; top: 161px; height: 202px; }
  .card--front-ceo { left: 626px; top: 408px; height: 202px; }

  .card__pattern {
    position: absolute; inset: 0;
    background: linear-gradient(135deg, var(--pattern-tint), var(--card-white) 50%, var(--pattern-line));
  }
  .wordmark {
    position: absolute;
    color: var(--text-dark);
    font-weight: 800;
    text-transform: uppercase;
    line-height: 0.95;
    letter-spacing: 0.5px;
  }
  .card--back .wordmark {
    left: 0; right: 0; top: 64px;
    text-align: center;
    font-size: 34px;
  }
  .card--front-md .wordmark,
  .card--front-ceo .wordmark {
    left: 14px; top: 18px;
    font-size: 18px;
  }
  .corner-swoosh { position: absolute; top: 0; right: 0; width: 130px; height: 145px; }
  .corner-swoosh path { fill: var(--brand-green); }

  .person {
    position: absolute;
    left: 0; width: 330px;
    text-align: center;
    margin-left: -4px;
  }
  .person__name {
    display: inline-block;
    color: var(--brand-green);
    font-size: 20px;
    font-weight: 600;
    padding: 0 2px 1px;
    border-bottom: 1.5px solid var(--brand-green);
    line-height: 1.1;
  }
  .person__role, .person__org {
    color: var(--text-grey);
    font-size: 11px;
    font-weight: 600;
    line-height: 1.15;
  }
  .card--front-md .person { top: 104px; }
  .card--front-md .person__role { margin-top: 5px; }
  .card--front-ceo .person { top: 104px; }
  .card--front-ceo .person__role { margin-top: 2px; }

  .contact {
    position: absolute;
    right: 10px;
    text-align: right;
    font-size: 11px;
    font-weight: 600;
    line-height: 1.4;
  }
  .card--front-md .contact { bottom: 8px; }
  .card--front-ceo .contact { bottom: 4px; }
  .contact__label, .contact__phone { color: var(--text-grey); }
  .contact__label { margin-bottom: 1px; }
  .contact__email { color: var(--brand-green); }
</style>
</head>
<body>
  <section class="card card--back" aria-label="Card back">
    <div class="card__pattern" role="img" aria-label="Light repeating arch line pattern in green on white"></div>
    <div class="wordmark">Vode Market<br>Yards</div>
  </section>

  <section class="card card--front-md" aria-label="Business card, Colin Bradshaw">
    <svg class="corner-swoosh" viewBox="0 0 130 145" aria-hidden="true">
      <path d="M0 0 H130 V140 C100 70 60 20 0 0 Z"/>
    </svg>
    <div class="wordmark">Vode Market<br>Yards</div>
    <div class="person">
      <div class="person__name">Colin Bradshaw</div>
      <div class="person__role">Managing Director</div>
    </div>
    <div class="contact">
      <div class="contact__email">colin@vodemarketyards.com.au</div>
    </div>
  </section>

  <section class="card card--front-ceo" aria-label="Business card, Martin Keogh">
    <svg class="corner-swoosh" viewBox="0 0 130 145" aria-hidden="true">
      <path d="M0 0 H130 V140 C100 70 60 20 0 0 Z"/>
    </svg>
    <div class="wordmark">Vode Market<br>Yards</div>
    <div class="person">
      <div class="person__name">Martin Keogh</div>
      <div class="person__role">Chief Executive Officer</div>
      <div class="person__org">VMY</div>
    </div>
    <div class="contact">
      <div class="contact__label">Phone</div>
      <div class="contact__phone">0400 137 952</div>
      <div class="contact__email">martin@vodemarketyards.com.au</div>
    </div>
  </section>
</body>
</html>
```